Vro Klinieken website for a maxillofacial surgery clinic

It's a website for a clinic for maxillofacial surgery in WordPress . The website doesn't need to be complicated but has to look professional. It needs to be in Dutch so i can give the texts. Similar websites are www.tandartsenpraktijkvelmor.nl or www.tbospecialisten.nl. Pages would be sort of similar to https://hetcentrumvoorgezichtszorg.nl/ or https://wolderveenclinics.nl/. Those lasts are maxillofacial surgery clinic websites, but there are little more extensive.
I uploaded the logo. If this is not the proper quality i can upload the eps. Logo was made through printhive.

Target Market(s)

Patients who can find me and see information about the clinic

Industry/Entity Type

Healthcare

Coding

Coded - Design and coding required

Number of Pages Required

5+ page

Font styles to use
Other font styles liked:
• Something standard professional

Colors
0054AA
0677BA
7BADD7
CADEEF
E8F1F8

Requirements
Nice to have
• Something in line with the logo. I prefer a little dark like the darker logos but I'm not sure if that's professional. Logos zbpor and gvls are instances i'm registered to so they will have to be on the website too but small somewhere.

```html
<!DOCTYPE html>
<html lang="en">
<head>
<meta charset="utf-8">
<title>Vro Klinieken</title>
<link href="https://fonts.googleapis.com/css2?family=Poppins:wght@400;500;600&display=swap" rel="stylesheet">
<style>
:root{
  --blue:#2ba3e2;
  --blue-dark:#1f8fd0;
  --slate:#5b6a8c;
  --text:#444a55;
  --light:#f4f5f7;
  --footer:#2e2f33;
  --white:#ffffff;
}
*{box-sizing:border-box;margin:0;padding:0}
html,body{width:1200px;height:4300px;overflow:hidden}
body{font-family:'Poppins',sans-serif;color:var(--text);background:var(--white);position:relative}
.abs{position:absolute}
a{color:inherit;text-decoration:none}
.btn{position:absolute;display:flex;align-items:center;justify-content:center;border-radius:30px;font-weight:600;color:var(--white);background:var(--blue)}
.btn-outline{background:transparent;border:2px solid var(--white)}

/* header */
.site-header{position:absolute;left:0;top:0;width:1200px;height:159px;background:var(--white)}
.brand{position:absolute;left:75px;top:38px;display:flex;align-items:center;gap:12px}
.brand-dot{width:34px;height:34px;border-radius:50%;background:var(--blue)}
.brand-name{font-size:34px;font-weight:500;color:var(--blue);line-height:1}
.header-phone{position:absolute;left:627px;top:33px;display:flex;align-items:center;gap:14px;font-weight:600;font-size:22px;color:var(--slate)}
.phone-badge{width:42px;height:42px;border-radius:50%;background:var(--slate);display:flex;align-items:center;justify-content:center}
.header-cta{left:880px;top:31px;width:247px;height:48px;font-size:17px}
.main-nav{position:absolute;left:315px;top:110px;display:flex;gap:41px;font-size:18px;color:#2d2f36}
.main-nav .active{color:var(--blue);font-weight:600}

/* hero */
.hero{position:absolute;left:0;top:159px;width:1200px;height:639px;background:linear-gradient(160deg,#c7ccd3 0%,#9aa5b3 40%,#6d8aa8 75%,#4c6f93 100%)}
.hero-title{position:absolute;left:0;width:1200px;top:160px;text-align:center;font-size:100px;font-weight:400;color:var(--white);letter-spacing:1px}
.hero-sub{position:absolute;left:160px;width:880px;top:275px;text-align:center;font-size:21px;font-weight:600;line-height:34px;color:var(--white)}
.hero-cta{left:502px;top:355px;width:196px;height:55px;font-size:20px}
.hero-dots{position:absolute;left:568px;top:587px;display:flex;gap:9px}
.hero-dots span{width:8px;height:8px;border-radius:50%;background:rgba(255,255,255,.6)}
.hero-dots span:first-child{background:var(--blue)}

/* welcome */
.welcome-kicker{left:80px;top:862px;font-size:46px;color:var(--slate);line-height:1}
.welcome-title{left:80px;top:908px;font-size:58px;color:var(--blue);line-height:1.05}
.welcome-text{left:75px;top:980px;width:520px;font-size:17px;line-height:31.5px;color:#333}
.welcome-cta{left:75px;top:1228px;width:198px;height:57px;font-size:20px}
.welcome-photo{left:616px;top:874px;width:511px;height:412px;background:linear-gradient(135deg,#8fb7d6,#4c88bd 60%,#376fa3);border-radius:60px 0 90px 0}

/* services */
.services{position:absolute;left:0;top:1362px;width:1200px;height:691px;background:linear-gradient(120deg,#3b78b4 0%,#4f86b9 45%,#6b98bf 100%)}
.services-title{position:absolute;left:0;width:1200px;top:58px;text-align:center;font-size:52px;color:var(--white)}
.service{position:absolute;top:155px;width:328px;text-align:center;color:var(--white)}
.service-photo{width:328px;height:243px;border-radius:26px 0 0 0}
.service h3{font-size:31px;font-weight:500;margin-top:22px}
.service p{font-size:15px;line-height:26px;margin:10px 8px 0}
.service .btn{position:relative;margin:22px auto 0;width:198px;height:57px;font-size:20px}

/* team */
.team-title{left:0;width:1200px;top:2112px;text-align:center;font-size:52px;color:var(--slate)}
.team-title span{color:var(--blue)}
.member{position:absolute;top:2215px;width:242px;text-align:center}
.member-photo{width:242px;height:228px;background:linear-gradient(160deg,#eef1f4,#c9d3dc)}
.member h4{font-size:22px;font-weight:500;color:var(--blue);margin-top:24px}
.member p{font-size:16px;line-height:25px;color:#444;margin-top:6px}

/* booking */
.booking{position:absolute;left:0;top:2637px;width:1200px;height:698px;background:linear-gradient(90deg,#2aa3e1 0%,#3b93d0 45%,#5c86b5 100%)}
.booking-photo{position:absolute;left:75px;top:79px;width:506px;height:469px;background:linear-gradient(135deg,#dbe6ee,#a9c2d6 55%,#6f98bc);border-radius:0 80px 0 80px}
.booking-card{position:absolute;left:524px;top:133px;width:603px;height:486px;background:var(--light);border-radius:60px 0 0 0;padding:22px 28px}
.booking-card h2{font-size:46px;font-weight:400;color:var(--slate)}
.booking-card h2 span{color:var(--blue)}
.field{position:absolute;height:52px;border:1px solid #cfd3d8;border-radius:26px;background:var(--white);font-size:15px;color:#444;padding:0 24px;display:flex;align-items:center}
.field.area{align-items:flex-start;padding-top:16px;border-radius:16px}
.select-arrow{position:absolute;right:22px;top:16px}
.submit{left:28px;top:388px;width:541px;height:54px;font-size:22px}

/* reviews */
.review-photo{left:75px;top:3408px;width:510px;height:410px;background:linear-gradient(135deg,#9ec3e0,#5a9bd1 55%,#3f7fb8);border-radius:60px 0 60px 0}
.reviews-title{left:613px;top:3418px;font-size:56px;color:var(--slate)}
.reviews-title span{color:var(--blue)}
.review-text{left:613px;top:3500px;width:520px;font-size:17px;line-height:31.5px;color:#333}
.review-avatar{left:615px;top:3710px;width:84px;height:84px;border-radius:50%;background:linear-gradient(135deg,#c9dbe9,#7ea9cf)}
.review-name{left:716px;top:3718px;font-size:22px;color:var(--blue)}
.review-loc{left:716px;top:3750px;font-size:19px;color:#444}
.review-dots{left:1052px;top:3745px;display:flex;gap:9px}
.review-dots span{width:12px;height:12px;border-radius:50%;background:#222}
.review-dots span:first-child{background:var(--blue)}

/* footer */
.site-footer{position:absolute;left:0;top:3894px;width:1200px;height:406px;background:var(--footer);color:var(--white)}
.footer-brand{position:absolute;left:75px;top:75px;display:flex;align-items:center;gap:10px}
.footer-brand .brand-name{font-size:28px}
.footer-brand .brand-dot{width:28px;height:28px}
.footer-legal{position:absolute;left:75px;top:220px;font-size:13px;line-height:28px}
.footer-social{position:absolute;left:75px;top:300px;display:flex;gap:20px}
.footer-social span{width:24px;height:24px;border-radius:50%;background:var(--white)}
.footer-col{position:absolute;top:72px}
.footer-col h5{font-size:21px;font-weight:600;margin-bottom:12px}
.footer-col li{list-style:none;font-size:15px;line-height:34px}
.hours li{display:flex}
.hours li b{font-weight:400;width:133px}
.contact li{display:flex;gap:16px;line-height:28px;margin-bottom:6px}
.contact svg{flex:none;margin-top:7px}
</style>
</head>
<body>

<header class="site-header">
  <div class="brand"><span class="brand-dot"></span><span class="brand-name">Vro Klinieken</span></div>
  <div class="header-phone">
    <span class="phone-badge"><svg width="20" height="20" viewBox="0 0 24 24" fill="#fff"><path d="M6.6 10.8a15 15 0 006.6 6.6l2.2-2.2c.3-.3.7-.4 1-.2 1.1.4 2.3.6 3.6.6.6 0 1 .4 1 1V20c0 .6-.4 1-1 1A17 17 0 013 4c0-.6.4-1 1-1h3.5c.6 0 1 .4 1 1 0 1.3.2 2.5.6 3.6.1.3 0 .7-.2 1z"/></svg></span>
    +31 79 555 0142
  </div>
  <a class="btn header-cta">Book An Appointment</a>
  <nav class="main-nav">
    <a class="active">Home</a><a>About Us</a><a>Treatments</a><a>Customer Stories</a><a>FAQ’s</a><a>Blog</a><a>Contact</a>
  </nav>
</header>

<section class="hero" role="img" aria-label="Surgeons treating a patient in a dental chair">
  <h1 class="hero-title">Vro Klinieken</h1>
  <p class="hero-sub">Sed ut perspiciatis unde omnis iste natus error sit &nbsp;voluptatem &nbsp;accusantium doloremque laudantium, totam rem aperiam.</p>
  <a class="btn hero-cta">Read More</a>
  <div class="hero-dots"><span></span><span></span><span></span></div>
</section>

<section class="welcome">
  <p class="abs welcome-kicker">Welcome to</p>
  <h2 class="abs welcome-title" style="font-weight:400">Vro Klinieken</h2>
  <p class="abs welcome-text">Sed ut perspiciatis unde omnis iste natus error sit voluptatem &nbsp;accusantium doloremque laudantium, totam rem aperiam, eaque ipsa quae ab illo inventore veritatis et quasi architecto beatae vitae dicta sunt explicaboemo enim ipsam voluptatem quia voluptas sit aspernatur aut odit aut fugit, sed quia consequuntur magni dolores eos qui ratione voluptatem sequi nesciunt.</p>
  <a class="btn welcome-cta">Read More</a>
  <div class="abs welcome-photo" role="img" aria-label="Skull model with dental instruments on a blue cloth"></div>
</section>

<section class="services" role="img" aria-label="Blue tinted clinic background">
  <h2 class="services-title" style="font-weight:400">Our Services</h2>
  <div class="service" style="left:75px">
    <div class="service-photo" role="img" aria-label="Oral surgery team treating a patient" style="background:linear-gradient(135deg,#8fc4e6,#4b98d3)"></div>
    <h3>Oral Surgery</h3>
    <p>Sed ut perspiciatis unde omnis iste natus error sit voluptatem accusantium doloremque laudantium.</p>
    <a class="btn btn-outline">Read More</a>
  </div>
  <div class="service" style="left:437px">
    <div class="service-photo" role="img" aria-label="Dentist examining a patient for sleep medicine" style="background:linear-gradient(135deg,#e6edf3,#3f7fc7)"></div>
    <h3>Sleep Medicine</h3>
    <p>Sed ut perspiciatis unde omnis iste natus error sit voluptatem accusantium doloremque laudantium.</p>
    <a class="btn btn-outline">Read More</a>
  </div>
  <div class="service" style="left:800px">
    <div class="service-photo" role="img" aria-label="Patient marked for facial plastic surgery" style="background:linear-gradient(135deg,#f3f5f7,#d9c3b6 50%,#9fbfdc)"></div>
    <h3>Plastic Surgery</h3>
    <p>Sed ut perspiciatis unde omnis iste natus error sit voluptatem accusantium doloremque laudantium.</p>
    <a class="btn btn-outline">Read More</a>
  </div>
</section>

<section class="team">
  <h2 class="abs team-title" style="font-weight:400">Meet Our <span>Team</span></h2>
  <div class="member" style="left:75px"><div class="member-photo" role="img" aria-label="Portrait of a dentist in a white coat"></div><h4>Name Heading</h4><p>Excepteur sint occaecat<br>cupidatat non</p></div>
  <div class="member" style="left:345px"><div class="member-photo" role="img" aria-label="Portrait of a doctor in a white coat"></div><h4>Name Heading</h4><p>Excepteur sint occaecat<br>cupidatat non</p></div>
  <div class="member" style="left:615px"><div class="member-photo" role="img" aria-label="Portrait of a doctor in a lab coat"></div><h4>Name Heading</h4><p>Excepteur sint occaecat<br>cupidatat non</p></div>
  <div class="member" style="left:885px"><div class="member-photo" role="img" aria-label="Portrait of a surgeon in blue scrubs" style="background:linear-gradient(160deg,#dfe8f0,#4d6fa8)"></div><h4>Name Heading</h4><p>Excepteur sint occaecat<br>cupidatat non</p></div>
</section>

<section class="booking">
  <div class="booking-photo" role="img" aria-label="Two smiling dental professionals"></div>
  <form class="booking-card">
    <h2>Book An <span>Appointment</span></h2>
    <div class="field" style="left:28px;top:103px;width:264px">Name</div>
    <div class="field" style="left:307px;top:103px;width:264px">Email Address</div>
    <div class="field" style="left:28px;top:170px;width:264px">Phone No</div>
    <div class="field" style="left:307px;top:170px;width:264px">Services Request
      <svg class="select-arrow" width="10" height="18" viewBox="0 0 10 18"><path d="M5 2l4 5H1zM5 16l4-5H1z" fill="#333"/></svg></div>
    <div class="field area" style="left:28px;top:237px;width:543px;height:130px">Phone No</div>
    <a class="btn submit">Submit</a>
  </form>
</section>

<section class="reviews">
  <div class="abs review-photo" role="img" aria-label="Smiling patient during a dental check-up"></div>
  <h2 class="abs reviews-title" style="font-weight:400">Customer <span>Reviews</span></h2>
  <p class="abs review-text">“&nbsp; Sed ut perspiciatis unde omnis iste natus error sit voluptatem &nbsp;accusantium doloremque laudantium, totam rem aperiam, eaque ipsa quae ab illo inventore veritatis et quasi architecto beatae vitae dicta sunt explicaboemo enim ipsam voluptatem quia voluptas sit aspernatur aut odit aut fugit, sed quia consequuntur..”</p>
  <div class="abs review-avatar" role="img" aria-label="Reviewer portrait"></div>
  <p class="abs review-name">Name Heading</p>
  <p class="abs review-loc">Location</p>
  <div class="abs review-dots"><span></span><span></span><span></span><span></span></div>
</section>

<footer class="site-footer">
  <div class="footer-brand"><span class="brand-dot"></span><span class="brand-name">Vro Klinieken</span></div>
  <p class="footer-legal">© Copyright 2023 Vro Klinieken<br>All Rights Reserved</p>
  <div class="footer-social"><span></span><span></span><span></span><span></span><span></span></div>

  <div class="footer-col" style="left:344px">
    <h5>Site Map</h5>
    <ul><li>Home</li><li>About Us</li><li>Treatments</li><li>Customer Stories</li><li>FAQ’s</li><li>Blog</li><li>Contact</li></ul>
  </div>
  <div class="footer-col hours" style="left:575px">
    <h5>Hours</h5>
    <ul>
      <li><b>Monday</b>08:15 - 17:15</li><li><b>Tuesday</b>08:15 - 17:15</li><li><b>Wednesday</b>08:15 - 17:15</li>
      <li><b>Thursday</b>08:15 - 17:15</li><li><b>Friday</b>08:15 - 17:15</li><li><b>Saturday</b>Closed</li><li><b>Sunday</b>Closed</li>
    </ul>
  </div>
  <div class="footer-col contact" style="left:885px;width:260px">
    <h5>Contact Info</h5>
    <ul>
      <li><svg width="16" height="14" viewBox="0 0 16 14"><path d="M1 2l4-1.5 6 2 4-1.5v11l-4 1.5-6-2-4 1.5z" fill="#fff"/></svg>Lindenhof 14, 2711 AB Noordveld, Nederland</li>
      <li><svg width="14" height="14" viewBox="0 0 24 24" fill="#fff"><path d="M6.6 10.8a15 15 0 006.6 6.6l2.2-2.2c.3-.3.7-.4 1-.2 1.1.4 2.3.6 3.6.6.6 0 1 .4 1 1V20c0 .6-.4 1-1 1A17 17 0 013 4c0-.6.4-1 1-1h3.5c.6 0 1 .4 1 1 0 1.3.2 2.5.6 3.6.1.3 0 .7-.2 1z"/></svg>+31 79 555 0142</li>
      <li><svg width="16" height="12" viewBox="0 0 16 12"><rect width="16" height="12" rx="1" fill="#fff"/><path d="M1 1l7 6 7-6" stroke="#2e2f33" stroke-width="1.5" fill="none"/></svg>info@vroklinieken.nl</li>
    </ul>
  </div>
</footer>

</body>
</html>
```